Professional, Elegant, Modern and Playful stationery design for an Orthodontist (Dentist)

We need a new stationery design for an Orthodontist (Dentist).
We would like to see designs that are elegant, but also playful. The designs and colors should be in harmony with the existing logo (uploaded).
The font of the logo text is roboto (Google), you don't need to use the same font, but the used font has to be in harmony with the font used in the logo and it has to be usable in Microsoft Word.
The colors used have to be in harmony with the logo.
The design for following parts are needed:
- A4 letter paper design
- A4 Microsoft Word Template (with and without letterhead)
- Envelope designs for C4 and C5 with the window on the right side
- CD/DVD-label design
- Stamping design

Target Market(s)

Orthodontist (Dentist)

Industry/Entity Type

It Professional

Font styles to use
Sans Serif

Colors

Designer to choose colors to be used in the design.

Requirements
Must have
• * Logo files are uploaded
• * A4 letter paper design: for printing press
• - Address position is on the right side
• - Needed Information in the letterhead:
• - Logo with company name as a unit
• or
• - separate the logo from the text and position them separately
• - Text needed:
• Kieferorthopädie Sonnhalde
• Dr. med. dent. Till Brösecke
• Fachzahnarzt für Kieferorthopädie (CH)
• Eidg. dipl. Zahnarzt, Mitglied VFP und BZR
• Wendelhofweg 7
• 8917 Lindenau
• 044 518 27 40
• (fax:)
• 044 518 27 41
• info@zahnbogen-praxis.example
• www.zahnbogen-praxis.example
• * A4 Microsoft Word Templates:
• - an empty and undesigned text example template is uploaded
• - the address lines are already correctly positioned behind the envelope window
• - design the positions of all elements
• - choose suitable fonts, which are in harmony with the font in the logo and the letterhead and which can be used in Microsoft Word (compatible with latest version, no old versions (.doc) needed)
• - choose suitable font sizes weights and colors, which are in harmony with the font in the logo and the letterhead.
• - One version with letterhead for printing on an empty paper
• - One version without letterhead for printing on a paper with letterhead already printed in printing press
• * Envelopes C4 and C5
• - window on the right side
• - Logo with company name (see uploaded files) as a unit
• or
• - Text needed:
• Wendelhofweg 7
• 8917 Lindenau
• * DVD/CD-label:
• or
• - Text needed:
• Wendelhofweg 7
• 8917 Lindenau
• 044 518 27 40
• info@zahnbogen-praxis.example
• www.zahnbogen-praxis.example
• - Patient name with birth date:
• Doe John, *1.2.1999
• - Two lines of text describing the contents on the CD/DVD
• * Stamping design:
• - Logo
• - Text:
• Kieferorthopädie Sonnhalde GmbH
• Wendelhofweg 7
• 8917 Lindenau
Should not have
• - Old Microsoft Word versions (.doc)

```html
<!DOCTYPE html>
<html lang="de">
<head>
<meta charset="utf-8">
<title>Kieferorthopädie Sonnhalde – Geschäftsausstattung</title>
<link rel="stylesheet" href="https://fonts.googleapis.com/css2?family=Roboto:wght@400;500;700&display=swap">
<style>
  :root{
    --backdrop:#cbcbcb;
    --paper:#ffffff;
    --paper-grey:#e5e5e5;
    --navy:#020066;
    --sky:#00adee;
    --ink:#222222;
    --muted:#777777;
    --shadow:#555555;
    --disc-hole:#666666;
  }
  *{margin:0;padding:0;box-sizing:border-box}
  html,body{width:1200px;height:1200px;overflow:hidden;background:var(--backdrop)}
  body{position:relative;font-family:"Roboto",Arial,sans-serif;color:var(--ink)}

  .sheet{position:absolute;box-shadow:3px 3px 0 var(--shadow);overflow:hidden}

  /* brand unit */
  .brand{position:absolute;display:flex;align-items:flex-start;gap:6px}
  .brand__dot{border-radius:50%;flex:none}
  .brand__name{font-weight:700;line-height:1.1}
  .brand__line{font-weight:400;line-height:1.2}

  /* letterhead */
  .letter{left:207px;top:177px;width:344px;height:486px;background:var(--paper)}
  .letter__web{position:absolute;left:22px;top:38px;font-size:7px;letter-spacing:.9px}
  .letter .brand{left:206px;top:24px}
  .letter .brand__dot{width:18px;height:18px;background:var(--navy);margin-top:2px}
  .letter .brand__name{font-size:6.4px;color:var(--navy)}
  .letter .brand__line{font-size:4.4px;color:var(--muted)}
  .letter__bar{position:absolute;left:0;top:427px;width:14px;height:44px;
    background:linear-gradient(90deg,var(--navy) 0 50%,var(--sky) 50% 100%)}
  .letter__foot{position:absolute;top:441px;font-size:6.6px;line-height:7.6px}
  .letter__foot--left{left:22px}
  .letter__foot--right{left:166px}

  /* folder & envelope */
  .folder{left:619px;top:154px;width:374px;height:531px;background:var(--paper-grey)}
  .envelope{left:619px;top:780px;width:374px;height:266px;background:var(--sky)}
  .bands{position:absolute;inset:0;width:100%;height:100%}
  .folder .brand{left:144px;top:30px}
  .folder .brand__dot{width:38px;height:38px;background:var(--navy)}
  .folder .brand__name{font-size:12.5px;color:var(--navy);margin-top:6px}
  .folder .brand__line{font-size:8.2px;color:var(--muted);letter-spacing:.3px}
  .envelope .brand{left:17px;top:56px}
  .envelope .brand__dot{width:27px;height:27px;background:var(--paper)}
  .envelope .brand__name{font-size:8.4px;color:var(--paper);margin-top:3px}
  .envelope .brand__line{font-size:5.2px;color:var(--paper)}

  .contact{position:absolute;left:55px;width:263px;color:var(--paper);font-size:6.6px}
  .folder .contact{top:482px}
  .envelope .contact{top:216px}
  .contact__row{display:flex;justify-content:space-between;white-space:nowrap}
  .contact__row + .contact__row{margin-top:6px}
  .contact__sep{border-left:1px solid var(--paper);height:9px;margin-top:-1px}
  .contact__web{justify-content:center;letter-spacing:4px;margin-top:8px!important}

  /* disc label */
  .disc{position:absolute;left:282px;top:816px;width:196px;height:196px;border-radius:50%;
    filter:drop-shadow(3px 3px 0 var(--shadow))}
</style>
</head>
<body>

<section class="sheet letter" aria-label="Briefbogen A4">
  <p class="letter__web">www.zahnbogen-praxis.example</p>
  <div class="brand">
    <span class="brand__dot"></span>
    <div>
      <p class="brand__name">Kieferorthopädie Sonnhalde</p>
      <p class="brand__line">Dr. med. dent. Till Brösecke</p>
      <p class="brand__line">Fachzahnarzt für Kieferorthopädie (CH)</p>
    </div>
  </div>
  <span class="letter__bar"></span>
  <p class="letter__foot letter__foot--left">Eidg. dipl. Zahnarzt, Mitglied VFP und BZR<br>Wendelhofweg 7<br>8917 Lindenau</p>
  <p class="letter__foot letter__foot--right">Phone.&nbsp;&nbsp; 044 518 27 40<br>Faxmile. 044 518 27 41<br>info@zahnbogen-praxis.example</p>
</section>

<section class="sheet folder" aria-label="Mappe">
  <svg class="bands" viewBox="0 0 374 531" preserveAspectRatio="none" aria-hidden="true">
    <polygon points="0,80 374,370 374,406 0,118" fill="var(--navy)"/>
    <polygon points="0,152 374,442 374,531 0,531" fill="var(--sky)"/>
  </svg>
  <div class="brand">
    <span class="brand__dot"></span>
    <div>
      <p class="brand__name">Kieferorthopädie Sonnhalde</p>
      <p class="brand__line">Dr. med. dent. Till Brösecke</p>
      <p class="brand__line">Fachzahnarzt für Kieferorthopädie (CH)</p>
    </div>
  </div>
  <div class="contact">
    <p class="contact__row"><span>Eidg. dipl. Zahnarzt, Mitglied VFP und BZR Wendelhofweg 7 8917 <b>Lindenau</b></span></p>
    <p class="contact__row"><span>Phone. 044 518 27 40</span><span class="contact__sep"></span><span>Faxmile. 044 518 27 41</span><span class="contact__sep"></span><span>info@zahnbogen-praxis.example</span></p>
    <p class="contact__row contact__web"><span>www.zahnbogen-praxis.example</span></p>
  </div>
</section>

<section class="sheet envelope" aria-label="Briefumschlag">
  <svg class="bands" viewBox="0 0 374 266" preserveAspectRatio="none" aria-hidden="true">
    <polygon points="149,0 374,0 374,176" fill="var(--paper-grey)"/>
    <polygon points="194,0 239,0 374,104 374,148" fill="var(--navy)"/>
  </svg>
  <div class="brand">
    <span class="brand__dot"></span>
    <div>
      <p class="brand__name">Kieferorthopädie Sonnhalde</p>
      <p class="brand__line">Dr. med. dent. Till Brösecke</p>
      <p class="brand__line">Fachzahnarzt für Kieferorthopädie (CH)</p>
    </div>
  </div>
  <div class="contact">
    <p class="contact__row"><span>Eidg. dipl. Zahnarzt, Mitglied VFP und BZR Wendelhofweg 7 8917 <b>Lindenau</b></span></p>
    <p class="contact__row"><span>Phone. 044 518 27 40</span><span class="contact__sep"></span><span>Faxmile. 044 518 27 41</span><span class="contact__sep"></span><span>info@zahnbogen-praxis.example</span></p>
    <p class="contact__row contact__web"><span>www.zahnbogen-praxis.example</span></p>
  </div>
</section>

<svg class="disc" viewBox="0 0 196 196" aria-label="CD-Label">
  <defs><clipPath id="disc-shape"><circle cx="98" cy="98" r="98"/></clipPath></defs>
  <g clip-path="url(#disc-shape)">
    <rect width="196" height="196" fill="var(--paper-grey)"/>
    <g transform="rotate(-40 98 98)">
      <rect x="-60" y="80" width="320" height="26" fill="var(--navy)"/>
      <rect x="-60" y="116" width="320" height="140" fill="var(--sky)"/>
      <circle cx="34" cy="58" r="7" fill="var(--navy)"/>
      <text x="46" y="56" font-size="6" font-weight="700" fill="var(--navy)" font-family="Roboto, sans-serif">Kieferorthopädie Sonnhalde</text>
      <text x="46" y="62" font-size="3.6" fill="var(--muted)" font-family="Roboto, sans-serif">Dr. med. dent. Till Brösecke</text>
      <text x="46" y="67" font-size="3.6" fill="var(--muted)" font-family="Roboto, sans-serif">Fachzahnarzt für Kieferorthopädie (CH)</text>
      <g font-size="3.3" fill="var(--paper)" font-family="Roboto, sans-serif" text-anchor="middle">
        <text x="98" y="140">Eidg. dipl. Zahnarzt, Mitglied VFP und BZR Wendelhofweg 7 8917 Lindenau</text>
        <text x="98" y="147">Phone. 044 518 27 40 | Faxmile. 044 518 27 41 | info@zahnbogen-praxis.example</text>
        <text x="98" y="155" letter-spacing="2.4">www.zahnbogen-praxis.example</text>
      </g>
    </g>
  </g>
  <circle cx="98" cy="98" r="34" fill="var(--disc-hole)"/>
</svg>

</body>
</html>
```